Pruett Design & Millwork needs a web presence. Looking for a unique Design so please submit an idea.

In brief, you should know the following about me: My company was established in 2001 and had been responsible for providing reasonable CAD Design and Custom Millwork ever since. My specialty is in the area Architectural CAD Design, Fabrication of Custom Millwork and Mouldings on a partime basis. Drawings and estimates done at a very reasonable cost. I look forward to working on your next project. Thanks in Advance, Glen 
I would like one page to show thumbnails linked to some of past millwork projects and another page with thumbnails linking to some of my house designs. I assume last page will have contact information accessed from a link on home page. I already had a logo designed which I can supply you with to design home page around. As I indicated I have a regular full time job and do this for additional income and will move to full time when I have enough business.

I have attached the logo I had designed in a couple different colors. I have also uploaded some PDF's of files that I also considered before choosing the RED LOGO to give an ideas of how we could tweak the logo to better fit the website if need be. Text is wrong in those.

Thanks,
Glen

I added my logo as a PDF side there seems to be a problem with scaling loge with the other file. Hope this helps.

Glen

Evening,
I will be hosting this site on servquill. Its looks like it will get launched with wordpress?  What will be involved from getting your design up so I can upload project pictures and and text to areas you have set aside? I am also going to upload a couple jpg of a couple recent projects so you can put in so I can get a feel of what they will look like. Thanks for all your work to date! Glen

I am not seeing alot of design variations or even many designers in fact. Is there something more from me you need? Do you need me to extend deadline?

Reason: It appears that your need some more time to submit some design changes. I will choose a design next week after changes have been submitted. Thanks for your time. Glen

Reason: Designers needs a couple days to submit some last minute changes. Thanks for all your submissions! Glen

Reason: Some last minute designs that I need to look at and give feedback on. I want to thank everyone for their designs and patience. Thanks again, Glen

Evening All,

Upon discussion with a couple of the designers I want the design done in Word Press and I have increased budget the amount they said they would need to do it for. Thanks for all submissions so far but I am still looking for the special one that stands out among the rest! Glen

I will not be extending deadline and choosing designer tomorrow morning so if you have anything else to add please do so tonight. Thanks for all your submissions. Glen

Target Market(s)

Millwork projects will be generally local where as CAD Design Projects could be emailed anywhere. Probably more USA but who knows.

Industry/Entity Type

House

Font styles to use
Other font styles liked:
• Eras Medium ITC, Calibri or Designers choice.

Requirements
Must have
• Must tie in my logo on Homepage at least. Could even be somewhat transparent in background? I will let the designer work that out.
Nice to have
• Page to point to current and past Design projects on one page and millwork on another.
Should not have
• Target a large Corporate or Global environment since it is a small business right now.

```html
<!DOCTYPE html>
<html lang="en">
<head>
<meta charset="utf-8">
<title>Pruett Design &amp; Millwork</title>
<link href="https://fonts.googleapis.com/css2?family=Quicksand:wght@500;600&family=Open+Sans:wght@400&display=swap" rel="stylesheet">
<style>
  :root {
    --page-white: #ffffff;
    --sky-deep: #3f7a8e;
    --sky-mid: #7fa9b8;
    --glass-pale: #c9d9df;
    --floor-tone: #9db6c0;
    --nav-bg: #3e535c;
    --home-bg: #1e333c;
    --panel-bg: rgba(61, 82, 92, 0.95);
    --panel-text: #c9d3d7;
    --heading-light: #ffffff;
    --label-dark: #3e535c;
    --strip-bg: rgba(255, 255, 255, 0.8);
    --thumb-border: #9a9a9a;
    --logo-ink: #2a3c44;
  }
  * { box-sizing: border-box; margin: 0; padding: 0; }
  html, body { width: 1200px; height: 997px; overflow: hidden; background: var(--page-white); }
  .canvas { position: relative; width: 1200px; height: 997px; overflow: hidden; background: var(--page-white); }

  .backdrop {
    position: absolute; inset: 0;
    background:
      linear-gradient(90deg, #ffffff 0%, #ffffff 13%, rgba(255,255,255,0) 30%, rgba(255,255,255,0) 76%, rgba(255,255,255,0.9) 92%, #ffffff 100%),
      radial-gradient(ellipse 360px 260px at 700px 40px, var(--sky-deep) 0%, rgba(63,122,142,0.6) 45%, rgba(63,122,142,0) 100%),
      radial-gradient(ellipse 300px 380px at 560px 880px, var(--floor-tone) 0%, rgba(157,182,192,0) 100%),
      radial-gradient(ellipse 260px 300px at 860px 760px, #b3c8d0 0%, rgba(179,200,208,0) 100%),
      linear-gradient(180deg, var(--sky-mid) 0%, var(--glass-pale) 30%, #e4ecef 55%, #c3d4da 72%, #dbe6ea 88%, #f4f7f8 100%);
  }

  .brand {
    position: absolute; left: 22px; top: 112px; width: 200px;
    display: flex; flex-direction: column; align-items: center; gap: 14px;
    font-family: "Quicksand", sans-serif; font-weight: 600; color: var(--logo-ink);
    text-align: center;
  }
  .brand-mark { width: 64px; height: 64px; background: var(--logo-ink); flex: none; }
  .brand-name { font-size: 24px; line-height: 1.2; }

  .main-nav {
    position: absolute; left: 277px; top: 116px; width: 894px; height: 43px;
    background: var(--nav-bg); display: flex; align-items: center;
    font-family: "Quicksand", sans-serif; font-weight: 500; font-size: 21px; color: var(--heading-light);
  }
  .nav-home { width: 72px; height: 43px; background: var(--home-bg); display: flex; align-items: center; justify-content: center; }
  .nav-item { position: absolute; top: 8px; transform: translateX(-50%); white-space: nowrap; }

  .welcome {
    position: absolute; left: 277px; top: 159px; width: 894px; height: 172px;
    background: var(--panel-bg);
  }
  .welcome h1 {
    position: absolute; left: 27px; top: 24px;
    font-family: "Quicksand", sans-serif; font-weight: 500; font-size: 30px; color: var(--heading-light);
    white-space: nowrap;
  }
  .welcome p {
    position: absolute; left: 23px; top: 72px; width: 832px;
    font-family: "Open Sans", sans-serif; font-size: 16.3px; line-height: 20px; color: var(--panel-text);
  }

  .recent-bar {
    position: absolute; left: 277px; top: 360px; width: 894px; height: 42px;
    background: var(--page-white);
  }
  .recent-bar h2 {
    position: absolute; left: 19px; top: 11px;
    font-family: "Quicksand", sans-serif; font-weight: 600; font-size: 16px; color: var(--label-dark);
  }
  .slider-arrows { position: absolute; left: 812px; top: 13px; }

  .recent-strip {
    position: absolute; left: 277px; top: 402px; width: 894px; height: 198px;
    background: var(--strip-bg);
  }
  .thumb {
    position: absolute; top: 25px; width: 186px; height: 142px;
    border: 1px solid var(--thumb-border);
  }
  .thumb-plan { background: linear-gradient(135deg, #ffffff, #ececec); }
  .thumb-house-dark { background: linear-gradient(180deg, #3f76a8 0%, #5a3a2a 45%, #4a3322 100%); }
  .thumb-house-yellow { background: linear-gradient(180deg, #3e7cbf 0%, #666a70 35%, #b88a2a 60%, #1c1c1c 100%); }
</style>
</head>
<body>
<div class="canvas">
  <div class="backdrop" role="img" aria-label="Architectural rendering of a modern glass building with line sketch overlay against a blue sky"></div>

  <div class="brand">
    <span class="brand-mark"></span>
    <span class="brand-name">Pruett Design<br>&amp; Millwork</span>
  </div>

  <nav class="main-nav">
    <a class="nav-home" aria-label="home">
      <svg width="22" height="20" viewBox="0 0 22 20"><path d="M11 1 L1 10 H4 V19 H9 V13 H13 V19 H18 V10 H21 Z" fill="#ffffff"/></svg>
    </a>
    <span class="nav-item" style="left:143px">about</span>
    <span class="nav-item" style="left:346px">millwork projects</span>
    <span class="nav-item" style="left:594px">house designs</span>
    <span class="nav-item" style="left:809px">contact us</span>
  </nav>

  <section class="welcome">
    <h1>Welcome to Pruett Design &amp; Millwork</h1>
    <p>Ut wisi enim ad minim veniam, quis nostrud exerci tation ullamcorper suscipit lobortis nisl ut aliquip ex ea commodo consequat. Duis autem vel eum iriure dolor in hendrerit in vulputate velit esse molestie consequat, vel illum dolore eu feugiat nulla facilisis a</p>
  </section>

  <div class="recent-bar">
    <h2>RECENT PROJECTS</h2>
    <svg class="slider-arrows" width="44" height="16" viewBox="0 0 44 16">
      <path d="M14 0 V16 L0 8 Z" fill="#333333"/>
      <path d="M28 0 V16 L42 8 Z" fill="#333333"/>
    </svg>
  </div>

  <div class="recent-strip">
    <div class="thumb thumb-plan" style="left:29px" role="img" aria-label="Floor plan drawing of a house design"></div>
    <div class="thumb thumb-house-dark" style="left:245px" role="img" aria-label="Rendering of a brown two-storey house with deck"></div>
    <div class="thumb thumb-plan" style="left:459px" role="img" aria-label="Floor plan drawing of a house design"></div>
    <div class="thumb thumb-house-yellow" style="left:674px" role="img" aria-label="Rendering of a yellow house with grey roof"></div>
  </div>
</div>
</body>
</html>
```